Ironvale Holdings Business card

We need a an amazing matte black and gold card! W are a finance investing company so we want something that's eye catching and sleek. We want it to be attractive and sleek and represent money. Heck with would like the letters and lgo to be printed as 24k gold one day. We have the logo added so please use the color scheme with the logo and have that beautifully placed on one side.

Target Market(s)

Investors of all ages

Industry/Entity Type

Financial

Contact Information for Business Card

Black and matte with gold lettering follow logo colrs please.

Font styles to use
Other font styles liked:
• you decide

Colors

Designer to choose colors to be used in the design.

Requirements
Must have
• Matte Black and Gold, logo on one side. job title and name , website, phone number and email address on the other side
Nice to have
• Matte black and crisp finish to attract investors
Should not have
• playful, very professional!

```html
<!DOCTYPE html>
<html lang="en">
<head>
<meta charset="UTF-8">
<title>Ironvale Holdings – Business Card</title>
<link rel="stylesheet" href="https://fonts.googleapis.com/css2?family=Cinzel:wght@500;600&family=Mulish:wght@400;500&display=swap">
<style>
  :root {
    --backdrop: #141416;
    --card-black: #1b1b1d;
    --gold-deep: #6e5a14;
    --gold-mid: #a88a1e;
    --gold-bright: #f0d54a;
    --gold-flat: #c9a62a;
    --ink-light: #f2f2f2;
  }
  * { margin: 0; padding: 0; box-sizing: border-box; }
  html, body {
    width: 1200px;
    height: 900px;
    overflow: hidden;
    background: var(--backdrop);
  }
  .canvas {
    position: relative;
    width: 1200px;
    height: 900px;
    display: flex;
    flex-direction: column;
    align-items: center;
    justify-content: center;
    gap: 44px;
  }
  .card {
    position: relative;
    width: 640px;
    height: 366px;
    padding: 22px;
    background: linear-gradient(120deg, var(--gold-deep) 0%, var(--gold-bright) 30%, var(--gold-mid) 55%, var(--gold-bright) 78%, var(--gold-deep) 100%);
    box-shadow: 0 14px 30px rgba(0,0,0,0.55);
  }
  .card-face {
    width: 100%;
    height: 100%;
    background: var(--card-black);
    position: relative;
  }
  .card-front .card-face {
    display: flex;
    align-items: center;
    justify-content: center;
  }
  .brand-name {
    font-family: "Cinzel", serif;
    font-weight: 600;
    font-size: 40px;
    letter-spacing: 2px;
    color: var(--gold-flat);
  }
  .card-back .card-face {
    display: flex;
    align-items: center;
    justify-content: center;
    padding-bottom: 30px;
  }
  .identity {
    text-align: right;
    padding-right: 20px;
  }
  .person-name {
    font-family: "Cinzel", serif;
    font-weight: 600;
    font-size: 33px;
    letter-spacing: 1px;
    background: linear-gradient(100deg, var(--gold-mid), var(--gold-bright) 50%, var(--gold-mid));
    -webkit-background-clip: text;
    background-clip: text;
    color: transparent;
    line-height: 1.1;
  }
  .person-role {
    font-family: "Mulish", sans-serif;
    font-size: 16px;
    color: var(--ink-light);
    margin-top: 8px;
    letter-spacing: 0.3px;
  }
  .divider {
    width: 1.5px;
    height: 74px;
    background: var(--ink-light);
  }
  .contacts {
    list-style: none;
    padding-left: 22px;
    font-family: "Mulish", sans-serif;
    font-size: 16px;
    color: var(--ink-light);
    letter-spacing: 0.3px;
  }
  .contacts li {
    display: flex;
    align-items: center;
    gap: 12px;
    height: 24px;
  }
  .contact-icon {
    width: 14px;
    height: 14px;
    flex: none;
  }
</style>
</head>
<body>
<main class="canvas">
  <section class="card card-front">
    <div class="card-face">
      <span class="brand-name">Ironvale Holdings</span>
    </div>
  </section>

  <section class="card card-back">
    <div class="card-face">
      <div class="identity">
        <div class="person-name">DANIEL REYES</div>
        <div class="person-role">Operational Manager</div>
      </div>
      <div class="divider"></div>
      <ul class="contacts">
        <li>
          <svg class="contact-icon" viewBox="0 0 14 14" aria-hidden="true">
            <rect x="3.5" y="0.8" width="7" height="12.4" rx="1.3" fill="none" stroke="#d9b93a" stroke-width="1.3"/>
            <circle cx="7" cy="11" r="0.8" fill="#d9b93a"/>
          </svg>
          +1 212 555 0187
        </li>
        <li>
          <svg class="contact-icon" viewBox="0 0 14 14" aria-hidden="true">
            <rect x="1" y="3" width="12" height="8.5" fill="#d9b93a"/>
            <path d="M1 3 L7 8 L13 3" fill="none" stroke="#1b1b1d" stroke-width="1.1"/>
          </svg>
          daniel.reyes@ironvale.com
        </li>
        <li>
          <svg class="contact-icon" viewBox="0 0 14 14" aria-hidden="true">
            <circle cx="7" cy="7" r="5.8" fill="#d9b93a"/>
            <ellipse cx="7" cy="7" rx="2.4" ry="5.8" fill="none" stroke="#1b1b1d" stroke-width="0.9"/>
            <line x1="1.2" y1="7" x2="12.8" y2="7" stroke="#1b1b1d" stroke-width="0.9"/>
          </svg>
          www.ironvale.com
        </li>
      </ul>
    </div>
  </section>
</main>
</body>
</html>
```